Business Card Re-design

We are looking for a fresh bold look for general office business cards. We are a staffing agency that staffs industrial, coal mining, and clerical jobs.
Tag Line: We match the RIGHT talent to the RIGHT roles.
Harlow Office: 2473 W. Tallow Creek Rd, Evansville, IN - 47308
p. 555.203.6180 f. 555.203.6195
Fenwick Office: 264 S. Birch Ln, Fenwick, IN - 47152
p. 555.319.2047 f. 555.203.6195
Absentee/Emergency 24hr Hotline 555.203.6172 opt.1
www.bluelanternworkforce.example

```html
<!DOCTYPE html>
<html lang="en">
<head>
<meta charset="utf-8">
<title>Blue Lantern Workforce – Business Cards</title>
<link href="https://fonts.googleapis.com/css2?family=Roboto:wght@400;500;700&display=swap" rel="stylesheet">
<style>
  :root {
    --page-bg: #e6e8eb;
    --card-white: #fbfbfb;
    --navy: #0f4a7c;
    --green: #3aaa4a;
    --ink: #2e2e2e;
    --back-deep: #2c4f8c;
    --back-light: #8fc6df;
    --white: #ffffff;
  }
  * { box-sizing: border-box; margin: 0; padding: 0; }
  html, body {
    width: 1200px; height: 1200px; overflow: hidden;
    background: var(--page-bg);
    font-family: "Roboto", Arial, sans-serif;
  }
  .card {
    position: absolute; left: 180px; width: 840px; height: 480px;
    box-shadow: 0 6px 18px rgba(0,0,0,.18);
  }
  .card-front { top: 80px; background: var(--card-white); }
  .card-back {
    top: 600px;
    background: linear-gradient(105deg, var(--back-deep) 0%, #4f7fae 45%, var(--back-light) 100%);
  }

  /* front: offices */
  .office { position: absolute; left: 40px; color: var(--ink); font-size: 15px; line-height: 21px; letter-spacing: .3px; }
  .office-north { top: 44px; }
  .office-south { top: 208px; }
  .office-title { color: var(--green); font-weight: 700; font-size: 17px; margin-bottom: 2px; letter-spacing: .4px; }
  .contact-line { display: flex; align-items: center; gap: 10px; margin-top: 4px; padding-left: 6px; }
  .contact-line svg { width: 14px; height: 14px; fill: var(--green); flex: none; }

  /* front: name block */
  .brand { position: absolute; right: 48px; top: 215px; display: flex; align-items: center; gap: 14px; }
  .brand-mark { width: 26px; height: 26px; background: var(--green); }
  .brand-name {
    color: var(--navy); font-weight: 700; font-size: 38px; line-height: 40px;
    text-transform: uppercase; letter-spacing: .5px;
  }
  .web {
    position: absolute; right: 48px; top: 366px;
    color: var(--navy); font-size: 16px; font-weight: 500; letter-spacing: .6px;
  }

  /* front: hotline band */
  .band { position: absolute; left: 0; right: 0; top: 402px; height: 30px; }
  .band-end { position: absolute; top: 0; height: 30px; width: 30px; background: var(--green); }
  .band-end.left { left: 0; } .band-end.right { right: 0; }
  .band-stripe { position: absolute; top: 0; height: 30px; width: 5px; background: var(--navy); }
  .band-bar {
    position: absolute; top: 0; left: 58px; right: 58px; height: 30px; background: var(--navy);
    color: var(--white); font-size: 15px; font-weight: 500; letter-spacing: .6px;
    display: flex; align-items: center; padding-left: 92px;
  }

  /* back */
  .tagline {
    position: absolute; left: 112px; top: 180px;
    color: var(--white); font-size: 22px; font-weight: 500; letter-spacing: .8px;
  }
  .back-brand { position: absolute; left: 470px; top: 250px; display: flex; align-items: center; gap: 16px; }
  .back-brand .brand-mark { background: var(--white); width: 30px; height: 30px; }
  .back-brand .brand-name { color: var(--white); font-size: 42px; line-height: 44px; }
</style>
</head>
<body>
  <section class="card card-front">
    <div class="office office-north">
      <p class="office-title">Harlow Office:</p>
      <p>2473 W. Tallow Creek Rd</p>
      <p>Harlow, IN - 47308</p>
      <p class="contact-line"><svg viewBox="0 0 24 24" aria-hidden="true"><path d="M6.6 10.8a15.1 15.1 0 0 0 6.6 6.6l2.2-2.2a1 1 0 0 1 1-.25 11.4 11.4 0 0 0 3.6.57 1 1 0 0 1 1 1V20a1 1 0 0 1-1 1A17 17 0 0 1 3 4a1 1 0 0 1 1-1h3.5a1 1 0 0 1 1 1c0 1.25.2 2.45.57 3.57a1 1 0 0 1-.25 1z"/></svg>555.203.6180</p>
      <p class="contact-line"><svg viewBox="0 0 24 24" aria-hidden="true"><path d="M6 2h10l2 2v4H6zM3 9h18a1 1 0 0 1 1 1v8h-4v4H6v-4H2v-8a1 1 0 0 1 1-1zm5 8v3h8v-3z"/></svg>555.203.6195</p>
    </div>
    <div class="office office-south">
      <p class="office-title">Fenwick Office:</p>
      <p>264 S. Birch Ln, Fenwick</p>
      <p>IN - 47152</p>
      <p class="contact-line"><svg viewBox="0 0 24 24" aria-hidden="true"><path d="M6.6 10.8a15.1 15.1 0 0 0 6.6 6.6l2.2-2.2a1 1 0 0 1 1-.25 11.4 11.4 0 0 0 3.6.57 1 1 0 0 1 1 1V20a1 1 0 0 1-1 1A17 17 0 0 1 3 4a1 1 0 0 1 1-1h3.5a1 1 0 0 1 1 1c0 1.25.2 2.45.57 3.57a1 1 0 0 1-.25 1z"/></svg>555.319.2047</p>
      <p class="contact-line"><svg viewBox="0 0 24 24" aria-hidden="true"><path d="M6 2h10l2 2v4H6zM3 9h18a1 1 0 0 1 1 1v8h-4v4H6v-4H2v-8a1 1 0 0 1 1-1zm5 8v3h8v-3z"/></svg>555.203.6195</p>
    </div>

    <div class="brand">
      <span class="brand-mark"></span>
      <p class="brand-name">Blue Lantern<br>Workforce</p>
    </div>
    <p class="web">www.bluelanternworkforce.example</p>

    <div class="band">
      <span class="band-end left"></span>
      <span class="band-stripe" style="left:38px"></span>
      <span class="band-stripe" style="left:47px"></span>
      <div class="band-bar">Absentee/Emergency 24hr Hotline 555.203.6172 opt.1</div>
      <span class="band-stripe" style="right:47px"></span>
      <span class="band-stripe" style="right:38px"></span>
      <span class="band-end right"></span>
    </div>
  </section>

  <section class="card card-back">
    <p class="tagline">We match the RIGHT talent to the RIGHT roles</p>
    <div class="back-brand">
      <span class="brand-mark"></span>
      <p class="brand-name">Blue Lantern<br>Workforce</p>
    </div>
  </section>
</body>
</html>
```